Breezeway Climate Business Card Design

Design new, 2 sides, business cards for a residential and light commercial heating, air conditioning contractor.

Target Market(s)

Homeowners, small businesses

Industry/Entity Type

Business

Contact Information for Business Card

Dominic Vasquerelli
Phone - 555-214-6837
Email
Address - PO box 618
Millbrook NJ 07999
Website - www.BreezewayClimateLLC.example

Requirements
Must have
• logo, company colors, standard size with no die cut, so I can use printhaven

```html
<!DOCTYPE html>
<html lang="en">
<head>
<meta charset="utf-8">
<title>Breezeway Climate Business Cards</title>
<link rel="stylesheet" href="https://fonts.googleapis.com/css2?family=Montserrat:wght@400;500;600&display=swap">
<style>
  :root {
    --backdrop: #2b2b2b;
    --card-dark: #1f1d1e;
    --card-light: #ffffff;
    --accent: #f7941d;
    --ink: #1c1c1c;
    --soft-white: #f2f2f2;
  }
  * { box-sizing: border-box; margin: 0; padding: 0; }
  html, body { width: 1200px; height: 900px; overflow: hidden; }
  body {
    background: var(--backdrop);
    font-family: "Montserrat", sans-serif;
    position: relative;
  }
  .card {
    position: absolute;
    left: 340px;
    width: 520px;
    height: 300px;
    border-radius: 22px;
    overflow: hidden;
    box-shadow: 0 12px 30px rgba(0,0,0,0.45);
  }
  .card-front { top: 110px; background: var(--card-dark); }
  .card-back { top: 490px; background: var(--card-light); }

  .brand {
    display: flex;
    align-items: center;
    gap: 10px;
    font-weight: 600;
    color: var(--accent);
    letter-spacing: 0.5px;
  }
  .brand-dot {
    width: 14px; height: 14px;
    border-radius: 50%;
    background: var(--accent);
  }
  .card-front .brand {
    position: absolute;
    left: 0; right: 0; top: 108px;
    justify-content: center;
    font-size: 30px;
  }
  .front-web {
    position: absolute;
    left: 0; right: 0; bottom: 36px;
    text-align: center;
    color: var(--soft-white);
    font-size: 17px;
    letter-spacing: 0.3px;
  }
  .front-web strong, .back-web strong { color: var(--accent); font-weight: 500; }

  .back-strip {
    position: absolute;
    left: 0; top: 0; bottom: 0;
    width: 48px;
    background: var(--card-dark);
  }
  .card-back .brand {
    position: absolute;
    right: 30px; top: 46px;
    font-size: 22px;
  }
  .contact {
    position: absolute;
    left: 72px; top: 118px;
    color: var(--ink);
  }
  .person-name {
    color: var(--accent);
    font-size: 22px;
    font-weight: 500;
    letter-spacing: 1px;
    text-transform: uppercase;
  }
  .person-title { font-size: 14px; margin-top: 2px; }
  .address { font-size: 14px; line-height: 18px; margin-top: 8px; padding-left: 18px; }
  .contact-list { list-style: none; margin-top: 6px; }
  .contact-list li {
    display: flex; align-items: center;
    font-size: 14px; line-height: 20px;
    margin-left: -36px;
    gap: 16px;
  }
  .icon {
    width: 16px; height: 16px;
    border-radius: 50%;
    background: var(--accent);
    display: flex; align-items: center; justify-content: center;
    flex: none;
  }
  .icon svg { width: 10px; height: 10px; }
</style>
</head>
<body>
  <section class="card card-front">
    <div class="brand"><span class="brand-dot"></span>Breezeway Climate</div>
    <p class="front-web">www.<strong>breezewayclimate</strong>.example</p>
  </section>

  <section class="card card-back">
    <div class="back-strip"></div>
    <div class="brand"><span class="brand-dot"></span>Breezeway Climate</div>
    <div class="contact">
      <p class="person-name">Marlon Teaberry</p>
      <p class="person-title">Director</p>
      <p class="address">P.O. Box 618<br>Millbrook, NJ 07999</p>
      <ul class="contact-list">
        <li><span class="icon"><svg viewBox="0 0 10 10"><path d="M2 1l2 2-1 1c.5 1.2 1.3 2 2.5 2.5l1-1 2 2-1 1.5C4 9 1 6 .5 2.5z" fill="#fff"/></svg></span>555-214-6837</li>
        <li><span class="icon"><svg viewBox="0 0 10 10"><rect x="3" y="1" width="4" height="8" rx="1" fill="none" stroke="#fff" stroke-width="1.2"/></svg></span>555-214-6890</li>
        <li><span class="icon"><svg viewBox="0 0 10 10"><rect x="1" y="2.5" width="8" height="5" fill="none" stroke="#fff" stroke-width="1"/><path d="M1 2.5l4 3 4-3" fill="none" stroke="#fff" stroke-width="1"/></svg></span>info@breezewayclimate.example</li>
        <li><span class="icon"><svg viewBox="0 0 10 10"><circle cx="5" cy="5" r="3.8" fill="none" stroke="#fff" stroke-width="1"/><path d="M1.2 5h7.6M5 1.2c-2 2.5-2 5.1 0 7.6M5 1.2c2 2.5 2 5.1 0 7.6" fill="none" stroke="#fff" stroke-width="0.8"/></svg></span><span class="back-web">www.<strong>breezewayclimate</strong>.example</span></li>
      </ul>
    </div>
  </section>
</body>
</html>
```